Mobile and Web design for Remote Skin Condition Service

A new web service that allows patients to upload photos for doctors to review. I need the designs for both mobile (NOT native app) and desktop versions. Key pages are provided in the mockups, and all major form elements are required.
Overall branding and design needed.

We are building an online system that allows patients to connect with a skin doctors.

Users will access the website (typically, but not exclusively via a mobile phone), register, upload photos, answer a few questions and pay to submit their details to a doctor.

The doctor will access the website via a desktop browser and review the case.

The patient’s user flow should be optimised for mobile. It should be usable on desktop too.

The doctor’s user flow should be optimised for desktop. It should be usable on mobile too.

Currently there are no branding restrictions, and no logo, so please be creative.

The site has to look professional, clean and easy to use.
There will be limited text on the pages.
Buttons should be prominent - but they should also obviously be buttons.

Attached are a selection of screens showing most of the functionality of the process - it is not all of the screens of the process but should give the developers enough range and examples.

Target Market(s)

Any user with a skin condition

Industry/Entity Type

Healthcare

Number of Pages Required

5+ page

Colors

Designer to choose colors to be used in the design.

Requirements
Must have
• Mobile and desktop versions of the key pages as per the brief.
• Should be obvious to use - eg the photo upload and camera functions should be standard

```html
<!DOCTYPE html>
<html lang="en">
<head>
<meta charset="UTF-8">
<title>Dermaly – Start your skin check</title>
<link rel="stylesheet" href="https://fonts.googleapis.com/css2?family=Open+Sans:wght@300;400;600;700&display=swap">
<style>
  :root {
    --teal: #6dbdbd;
    --teal-light: #d8f1f1;
    --teal-border: #d9f0ef;
    --navy: #1f3341;
    --ink: #3e4a53;
    --muted: #7d8a93;
    --heading: #6b7883;
    --hero-bg: #f9fafa;
    --page-bg: #eef1f2;
    --white: #ffffff;
    --link: #2b8ad6;
  }
  * { box-sizing: border-box; margin: 0; padding: 0; }
  html, body {
    width: 734px;
    height: 1200px;
    overflow: hidden;
    background: var(--page-bg);
    font-family: "Open Sans", Arial, sans-serif;
  }
  .screen {
    position: absolute;
    left: 107px;
    top: 25px;
    width: 520px;
    height: 1150px;
    background: var(--white);
    box-shadow: 0 6px 30px rgba(30, 50, 60, 0.08);
  }
  .site-header {
    height: 75px;
    display: flex;
    align-items: center;
    padding: 0 23px;
  }
  .brand {
    font-weight: 700;
    font-size: 20px;
    letter-spacing: 2px;
    color: var(--teal);
  }
  .header-actions {
    margin-left: auto;
    display: flex;
    gap: 11px;
    align-items: center;
  }
  .btn-login {
    width: 99px;
    height: 39px;
    border: none;
    border-radius: 6px;
    background: var(--teal);
    color: var(--white);
    font-family: inherit;
    font-size: 16px;
    font-weight: 600;
  }
  .btn-menu {
    width: 44px;
    height: 41px;
    border: 1.5px solid var(--teal);
    border-radius: 6px;
    background: var(--white);
    display: flex;
    align-items: center;
    justify-content: center;
  }
  .hero {
    height: 293px;
    background: var(--hero-bg);
    display: flex;
    align-items: center;
    justify-content: center;
  }
  .hero-art {
    width: 246px;
    height: 246px;
    border-radius: 50%;
    background: radial-gradient(circle at 50% 45%, var(--teal-light) 0%, #eef8f8 55%, var(--white) 75%);
    box-shadow: inset 0 -4px 0 #a9d6d7;
  }
  .intro {
    text-align: center;
    padding: 0 29px;
  }
  .intro h1 {
    margin-top: 38px;
    font-weight: 300;
    font-size: 35px;
    line-height: 46px;
    color: var(--heading);
  }
  .intro p {
    margin-top: 24px;
    font-weight: 300;
    font-size: 18px;
    line-height: 30px;
    color: var(--muted);
  }
  .steps {
    list-style: none;
    margin: 26px 23px 0;
    height: 339px;
    border: 1.5px solid var(--teal-border);
    border-radius: 6px;
    padding: 22px 0 0 26px;
  }
  .step {
    display: flex;
    align-items: center;
    height: 62px;
    font-size: 19px;
    color: var(--ink);
  }
  .step-number {
    width: 37px;
    height: 37px;
    border-radius: 50%;
    background: var(--teal);
    box-shadow: 0 0 0 3px #e4f4f4;
    color: var(--white);
    font-weight: 700;
    font-size: 18px;
    display: flex;
    align-items: center;
    justify-content: center;
    margin-right: 20px;
  }
  .btn-start {
    display: block;
    margin: 22px 23px 0;
    width: calc(100% - 46px);
    height: 68px;
    border: none;
    border-radius: 6px;
    background: var(--navy);
    color: var(--white);
    font-family: inherit;
    font-size: 21px;
    font-weight: 600;
  }
  .legal {
    margin-top: 16px;
    padding: 0 22px;
    text-align: center;
    font-size: 13px;
    line-height: 20px;
    font-weight: 700;
    color: var(--navy);
  }
  .legal a { color: var(--link); }
</style>
</head>
<body>
  <main class="screen">
    <header class="site-header">
      <span class="brand">DERMALY</span>
      <div class="header-actions">
        <button class="btn-login">Login</button>
        <button class="btn-menu" aria-label="Menu">
          <svg width="24" height="18" viewBox="0 0 24 18">
            <g stroke="#6dbdbd" stroke-width="2" stroke-linecap="round">
              <line x1="1" y1="2" x2="23" y2="2"/>
              <line x1="1" y1="9" x2="23" y2="9"/>
              <line x1="1" y1="16" x2="23" y2="16"/>
            </g>
          </svg>
        </button>
      </div>
    </header>

    <section class="hero">
      <div class="hero-art" role="img" aria-label="Medical cross emblem in a soft teal circle"></div>
    </section>

    <section class="intro">
      <h1>A Short Catchy Headline</h1>
      <p>There are many variations of passages of Lorem Ipsum available, but the majority have suffered alteration in some form, by injected humour, or randomised words which don't look even slightly believable.</p>
    </section>

    <ol class="steps">
      <li class="step"><span class="step-number">1</span>Take or upload 3 photos</li>
      <li class="step"><span class="step-number">2</span>Tell us a little about yourself</li>
      <li class="step"><span class="step-number">3</span>Answer a few medical questions</li>
      <li class="step"><span class="step-number">4</span>Make a secure online payment</li>
      <li class="step"><span class="step-number">5</span>Wait just 24hours for your diagnosis</li>
    </ol>

    <button class="btn-start">Ready to Start?</button>

    <p class="legal">*By selecting "Ready to Start?", you agree to our <a href="#">Terms of Service</a> (including the mandatory arbitration of disputes) and consent to our <a href="#">Privacy Policy.</a></p>
  </main>
</body>
</html>
```